Ecommerce site for Curtain Track Company

This is an ecommerce store design and will be based on the xcart ecommerce platform, attached is a design specification and all images to use in the design, you may use any other images you see fit.
This is a new Company so has no logo, if possible please create a logo but if not just use a text based logo in the design this maybe replaced later if required.
We only require a Home page design initially but will also need a category and product page design created, if you can do those also it would be an advantage.
IMPORTANT
We require all designs to be supplied as a full size JPG so we can see the design in detail as the pixel harbor previews are often too small.

```html
<!DOCTYPE html>
<html lang="en">
<head>
<meta charset="utf-8">
<title>Cove Rails – Curtain Tracks</title>
<link rel="stylesheet" href="https://fonts.googleapis.com/css2?family=Titillium+Web:wght@700&family=Arimo:wght@400;700&family=Asap+Condensed:ital,wght@0,400;1,400&display=swap">
<style>
:root{
  --page-top:#f7f7f7;
  --page-bottom:#dcdcdc;
  --brand:#6a5494;
  --nav:#5e4880;
  --lavender-light:#d7d0e4;
  --lavender-mid:#8b74ad;
  --purple-deep:#5b4580;
  --menu-active:#d7d0e4;
  --menu-text:#707070;
  --ink:#333;
  --white:#fff;
}
*{box-sizing:border-box;margin:0;padding:0}
html,body{width:1200px;height:782px;overflow:hidden}
body{
  background:linear-gradient(var(--page-top),var(--page-bottom));
  font-family:"Arimo",Arial,sans-serif;
  position:relative;
}
.logo{
  position:absolute;left:147px;top:24px;
  font-family:"Titillium Web",sans-serif;font-weight:700;
  font-size:50px;letter-spacing:-1.5px;color:var(--brand);
}
.search{
  position:absolute;left:900px;top:19px;width:153px;height:24px;
  background:var(--lavender-light);display:flex;
}
.search span{flex:1;font-size:13px;color:#4a3a66;padding:4px 8px}
.search .go{width:25px;border-left:1px solid #fff;display:flex;align-items:center;justify-content:center}
.cart{
  position:absolute;right:147px;top:58px;text-align:right;
  font-size:10px;color:var(--ink);line-height:12px;
}
.cart b{color:#4a3a66}
.cart .links a{color:var(--ink);text-decoration:underline;margin-left:12px}
.shell{
  position:absolute;left:148px;top:110px;width:906px;height:634px;
  box-shadow:0 0 6px rgba(0,0,0,.25);
}
.nav{
  height:37px;background:var(--nav);display:flex;justify-content:center;align-items:center;
  font-size:10.5px;color:var(--white);letter-spacing:.4px;padding-left:30px;
}
.nav span.sep{margin:0 12px}
.sidebar{
  position:absolute;left:0;top:37px;width:173px;height:305px;background:var(--white);
}
.sidebar ul{list-style:none;margin-top:43px}
.sidebar li{height:33px;line-height:33px;padding-left:18px;font-size:13.5px;color:var(--menu-text);margin-bottom:15px}
.sidebar li.active{background:var(--menu-active);color:var(--ink)}
.hero{
  position:absolute;left:173px;top:37px;width:733px;height:305px;
  background:linear-gradient(180deg,#c9c6bf 0%,#e9eee8 18%,#bfd3cc 45%,#1e5a63 60%,#dfe6e2 88%,#c6a98a 100%);
}
.pay{
  position:absolute;left:0;top:342px;width:173px;height:285px;background:var(--lavender-light);
  border-bottom:8px solid var(--nav);
}
.cards{position:absolute;left:33px;top:86px;width:106px;display:grid;grid-template-columns:50px 50px;gap:4px 6px}
.card{height:31px;background:var(--white);border:1px solid #9a9a9a;font-size:8px;font-weight:700;color:var(--nav);display:flex;align-items:center;justify-content:center}
.card.wide{grid-column:1/3;width:84px;height:31px;margin:6px auto 0}
.perks{
  position:absolute;left:173px;top:342px;width:366px;height:292px;background:var(--lavender-mid);
  font-family:"Asap Condensed",sans-serif;font-style:italic;color:var(--white);font-size:19.5px;line-height:18px;
  padding:48px 0 0 26px;list-style:none;
}
.perks li{padding-left:10px;text-indent:-10px;margin-bottom:20px}
.about{
  position:absolute;left:539px;top:342px;width:367px;height:292px;background:var(--purple-deep);
  font-family:"Asap Condensed",sans-serif;color:var(--white);font-size:12.5px;line-height:18px;
  padding:58px 31px 0 32px;text-align:justify;
}
.about p+p{margin-top:6px}
</style>
</head>
<body>
<div class="logo">Cove Rails</div>
<div class="search"><span>search...</span><div class="go">
<svg width="14" height="14" viewBox="0 0 14 14"><circle cx="5.5" cy="5.5" r="4" fill="none" stroke="#4a3a66" stroke-width="2"/><line x1="8.5" y1="8.5" x2="12.5" y2="12.5" stroke="#4a3a66" stroke-width="2.4"/></svg></div></div>
<div class="cart">
  <div><b>CART: 2 products</b></div>
  <div>Total price: <b>$100</b></div>
  <div class="links"><a>view cart »</a><a>check cart »</a></div>
</div>
<div class="shell">
  <nav class="nav">
    <span>HOME</span><span class="sep">|</span><span>ABOUT US</span><span class="sep">|</span><span>DELIVERY TERMS</span><span class="sep">|</span><span>TESTIMONIALS</span><span class="sep">|</span><span>FAQ'S</span><span class="sep">|</span><span>CONTACT US</span>
  </nav>
  <aside class="sidebar"><ul>
    <li class="active">Quiet Glide Tracks</li>
    <li>Hand operated Tracks</li>
    <li>Cord operated Tracks</li>
    <li>Automated Tracks</li>
  </ul></aside>
  <div class="hero" role="img" aria-label="Photo of a bright hall with tall windows, white columns and long teal curtains on ceiling tracks"></div>
  <div class="pay"><div class="cards">
    <div class="card">Vantra</div><div class="card">Meridian</div>
    <div class="card">Pathway</div><div class="card">Crestline</div>
    <div class="card wide">PayLoop</div>
  </div></div>
  <ul class="perks">
    <li>• Free UK delivery on orders over £100</li>
    <li>• Over 20 years experience measuring / making / fitting</li>
    <li>• 5 years guarantee on all quiet glide products</li>
    <li>• Friendly family run business</li>
  </ul>
  <div class="about">
    <p>From our Worcestershire factory we have been supplying quality product to British customers for over 30 years. We pride ourselves on the fact that whilst we refuse to compromise on quality, we still manage to offer our product at unbeatable prices.</p>
    <p>We take immense pride in our made to measure wooden venetian blinds, as well as our entire window decor range. When you think of made to measure wooden venetian blinds, think of us.</p>
  </div>
</div>
</body>
</html>
```